Corvane Industries business cards

We need business cards for our company Corvane Industries, based in Brisbane but trading world wide. We buy and sell Corvane Industries, generators and marine equipment. The design needs to be kept clean, simple but eye catching.
Please keep with our current logo (included) and further information can be included on request

Business

0792cd
33a6d7
85cae6
3276b5
0455a3
cedeed
cee9f5
ffffff

```html
<!DOCTYPE html>
<html lang="en">
<head>
<meta charset="utf-8">
<title>Corvane Industries business cards</title>
<link rel="stylesheet" href="https://fonts.googleapis.com/css2?family=Mulish:wght@400;700;800&display=swap">
<style>
  :root {
    --backdrop: #d4d6d9;
    --brand-blue: #3276b5;
    --brand-deep: #0455a3;
    --brand-mid: #33a6d7;
    --brand-soft: #85cae6;
    --brand-pale: #cee9f5;
    --brand-mist: #cedeed;
    --paper: #ffffff;
    --ink: #4a4a4a;
    --ink-soft: #5c5c5c;
  }
  html, body {
    margin: 0;
    width: 1200px;
    height: 871px;
    overflow: hidden;
    background: var(--backdrop);
    font-family: "Mulish", sans-serif;
  }
  .canvas {
    position: relative;
    width: 1200px;
    height: 871px;
  }
  .card {
    position: absolute;
    width: 560px;
    height: 320px;
    border-radius: 4px;
    box-shadow: 0 12px 30px rgba(0,0,0,.22);
    overflow: hidden;
  }
  /* Front: blue side */
  .card-front {
    left: 80px;
    top: 90px;
    background: linear-gradient(160deg, #5a93c8 0%, var(--brand-blue) 55%, #2a68a6 100%);
    color: var(--paper);
  }
  .front-monogram {
    position: absolute;
    left: 250px;
    top: 30px;
    font-weight: 800;
    font-size: 200px;
    line-height: 1;
    letter-spacing: -6px;
    color: rgba(255,255,255,.09);
  }
  .front-monogram-sub {
    position: absolute;
    left: 420px;
    top: 228px;
    font-size: 24px;
    font-weight: 700;
    color: rgba(255,255,255,.12);
  }
  .front-mark {
    position: absolute;
    left: 70px;
    top: 125px;
    width: 70px;
    height: 70px;
    border-radius: 10px;
    background: var(--paper);
  }
  .front-web {
    position: absolute;
    left: 168px;
    top: 148px;
    font-size: 15px;
    letter-spacing: .5px;
    color: rgba(255,255,255,.9);
  }
  /* Back: white side */
  .card-back {
    left: 560px;
    top: 460px;
    background: var(--paper);
    color: var(--ink);
  }
  .back-accent {
    position: absolute;
    right: 60px;
    top: 40px;
    width: 120px;
    height: 120px;
    background: var(--brand-mist);
    opacity: .45;
  }
  .holder-name {
    position: absolute;
    left: 40px;
    top: 34px;
    margin: 0;
    font-size: 17px;
    font-weight: 700;
    color: var(--ink);
  }
  .address {
    position: absolute;
    left: 40px;
    top: 76px;
    margin: 0;
    font-size: 12.5px;
    line-height: 1.5;
    font-style: normal;
    color: var(--ink-soft);
  }
  .contact-list {
    position: absolute;
    left: 40px;
    top: 150px;
    margin: 0;
    padding: 0;
    list-style: none;
    font-size: 12.5px;
    color: var(--ink-soft);
  }
  .contact-list li {
    display: flex;
    align-items: center;
    gap: 12px;
    height: 21px;
  }
  .contact-list svg {
    width: 13px;
    height: 13px;
    fill: none;
    stroke: var(--brand-blue);
    stroke-width: 1.6;
  }
  .brand-lockup {
    position: absolute;
    right: 34px;
    bottom: 40px;
    display: flex;
    align-items: center;
    gap: 12px;
  }
  .brand-square {
    width: 46px;
    height: 46px;
    border-radius: 7px;
    background: var(--brand-blue);
  }
  .brand-name {
    font-size: 24px;
    font-weight: 700;
    line-height: 1;
    color: var(--brand-blue);
  }
</style>
</head>
<body>
<main class="canvas">
  <section class="card card-front" aria-label="Card front">
    <div class="front-monogram" aria-hidden="true">CI</div>
    <div class="front-monogram-sub" aria-hidden="true">Pty Ltd</div>
    <div class="front-mark" aria-hidden="true"></div>
    <div class="front-web">www.corvaneind.com.au</div>
  </section>

  <section class="card card-back" aria-label="Card back">
    <div class="back-accent" aria-hidden="true"></div>
    <h1 class="holder-name">Marla Kestrel</h1>
    <address class="address">
      18 Tallow Street, Eastvale QLD 4100<br>
      PO Box 512, Northgate<br>
      QLD 4013
    </address>
    <ul class="contact-list">
      <li>
        <svg viewBox="0 0 14 14"><path d="M2 5c0-2 3-3 5-3s5 1 5 3l-2 1-1-2H5L4 6z M3 8h8v4H3z"/></svg>
        +61 7 3000 4821
      </li>
      <li>
        <svg viewBox="0 0 14 14"><rect x="4" y="1" width="6" height="12" rx="1"/><line x1="6" y1="11" x2="8" y2="11"/></svg>
        +61 400 555 219
      </li>
      <li>
        <svg viewBox="0 0 14 14"><rect x="4" y="1" width="6" height="4"/><rect x="1.5" y="5" width="11" height="5" rx="1"/><rect x="4" y="9" width="6" height="4"/></svg>
        +61 7 3000 4822
      </li>
      <li>
        <svg viewBox="0 0 14 14"><rect x="1" y="3" width="12" height="8"/><path d="M1 3l6 5 6-5"/></svg>
        marla@corvaneind.com.au
      </li>
    </ul>
    <div class="brand-lockup">
      <div class="brand-square" aria-hidden="true"></div>
      <div class="brand-name">Corvane Industries</div>
    </div>
  </section>
</main>
</body>
</html>
```